Consulting physiotherapist requires website update using existing Word Press template and developmen

PLEASE ENSURE YOU SEE THE NEW WEBSITE WHICH ONLY WENT LIVE IN THE LAST FORTNIGHT. GOOGLE SEEMS TO BE STILL BRING UP THE OLD WEBSITE. PLEASE USE http://www.tallowcreekqld.com.au/index.php TO ENSURE YOU SEE THE NEW WEBSITE WITH NEW LOGO USING GREEN LEAVES.

Tallow Creek has a new website that was developed by a family friend using a Word Press template. The content, layout, colour and images need to be updated. It is important that I retain control of the website so that content can be regularly updates. I would like a blogging page that is synchronised with my linked in and facebook pages. A new logo was designed in January this year and this needs to be integrated into all corporate materials including business card, services brochure and quoting templates.

See existing website and attached brochure for product and services details. www.tallowcreekqld.com.au

Tallow creek is a boutique consultancy offering injury prevention and injury management services, predominantly throughout Queensland. The Principal Consultant, Marisa Pendry, is a Physiotherapist and Occupational Health Consultant with 18 years experience.

Marisa is proud of the high quality service she delivers for her clients. She intends to retain the boutique consultancy at its current size in order to maintain client relationships and continue to deliver high-quality, outcome focussed and evidence-based strategies to promote the health of workers and in turn, the success of business.

The website should reflect the values of Tallow creek, which is to deliver customised, targeted programs to promote worker health and business success. Tallow creek does not offer generic products or services. We identify the client’s needs, whether the client is the employer or the employee, and provide advice and services to target that need.

We are approachable and friendly. Our training services are fun and engaging, backed up by solid medical and scientific evidence. Our management of injured workers is offered with genuine care and compassion, while acknowledging and supporting the needs of business to continue operating successfully and profitably.

Our ergonomics and safety consulting services aim to achieve the ‘holy grail’ – improving worker health and productivity and in turn, promoting the success of business.

Target Market(s)

HR Managers and Safety Professionals

Industry/Entity Type

Health Care

Contact Information for Business Card

Marisa Pendry
Occupational Health Consultant & Physiotherapist
B.Phty | G.Dip.Erg | G.Cert OH&S
PO Box 47
Camp Hill QLD 4152
07 3261 5904
0417 685 390

Number of Pages Required

5+ page

Colors
cadf82
abd037
9bcb3c

Requirements
Must have
• Designer must be able to work with existing WordPress template. I would like to be able to update my own content in the future and can only do this within a simple template.

```html
<!DOCTYPE html>
<html lang="en">
<head>
<meta charset="utf-8">
<title>Tallow creek – Injury Prevention &amp; Management</title>
<link href="https://fonts.googleapis.com/css2?family=Open+Sans:wght@400;600;700&amp;family=Cabin:wght@400;500&amp;family=Merriweather:wght@700&amp;display=swap" rel="stylesheet">
<style>
:root{
  --green:#9bcb3c;
  --green-mid:#abd037;
  --green-light:#cadf82;
  --green-dark:#2f5e34;
  --ink:#333;
  --muted:#777;
  --pale:#f1f2ef;
  --darker:#1e2120;
  --white:#fff;
}
*{box-sizing:border-box;margin:0;padding:0}
html,body{width:1200px;height:2680px;overflow:hidden}
body{font-family:"Open Sans",Arial,sans-serif;color:var(--ink);background:var(--white);position:relative;font-size:12px;line-height:1.6}
.abs{position:absolute}

/* header */
.site-header{left:0;top:0;width:1200px;height:140px;background:var(--white)}
.brand{left:60px;top:22px;display:flex;align-items:center;gap:12px}
.brand-dot{width:50px;height:50px;border-radius:50%;background:var(--green)}
.brand-name{font-family:"Cabin",sans-serif;font-size:40px;color:var(--green-dark);line-height:1}
.brand-tag{font-size:13px;font-weight:600;color:var(--green-dark);letter-spacing:.4px}
.top-phone{right:75px;top:20px;font-size:13px;color:var(--ink);display:flex;align-items:center;gap:6px}
.main-nav{right:75px;top:70px;display:flex}
.main-nav a{display:block;padding:8px 18px;font-size:13px;color:var(--ink);text-decoration:none;border-left:1px solid #e3e3e3}
.main-nav a:first-child{border-left:0}
.main-nav a.active{color:var(--green-dark);border-bottom:2px solid var(--green)}

/* hero */
.hero{left:0;top:140px;width:1200px;height:470px;background:linear-gradient(120deg,#d9dfe1 0%,#b9c6cb 35%,#8e9ea5 65%,#c8d1d3 100%)}
.hero-title{left:590px;top:250px;font-family:"Cabin",sans-serif;font-size:34px;color:var(--white)}
.hero-text{left:590px;top:300px;width:560px;font-size:13px;color:var(--white)}
.hero-arrow{top:215px;width:34px;height:34px;border-radius:50%;background:rgba(255,255,255,.35)}

/* welcome */
.welcome{left:88px;top:600px;width:1064px;height:320px;background:var(--white);box-shadow:0 4px 18px rgba(0,0,0,.12)}
.video{left:14px;top:24px;width:380px;height:220px;background:linear-gradient(135deg,#c6cfd1,#8a969a)}
.video-bar{left:14px;top:244px;width:380px;height:26px;background:#222}
.video-bar i{position:absolute;left:34px;top:12px;width:300px;height:3px;background:#555}
.video-bar b{position:absolute;left:34px;top:12px;width:70px;height:3px;background:var(--green)}
.welcome-body{left:420px;top:20px;width:620px}
.sec-head{display:flex;align-items:center;gap:10px}
.sec-dot{width:38px;height:38px;border-radius:50%;background:var(--green)}
.sec-title{font-family:"Cabin",sans-serif;font-weight:400;font-size:38px;color:var(--ink);line-height:1.1}
.sec-sub{font-size:13px;color:var(--green-dark);margin-left:48px}
.welcome-body p{font-size:12.5px;color:#555;margin-top:12px}
.btn{display:inline-block;background:var(--green-dark);color:var(--white);font-size:12px;padding:7px 18px;border-radius:3px}

/* services */
.services{left:0;top:950px;width:1200px;height:590px;background:var(--pale)}
.center-head{left:0;width:1200px;text-align:center}
.center-head .sec-head{justify-content:center}
.center-head .sec-sub{margin-left:48px}
.card{top:150px;width:240px}
.photo-ring{width:170px;height:170px;border-radius:50%;border:5px solid var(--white);box-shadow:0 0 0 3px var(--green-light);margin:0 auto 26px}
.card h3{font-family:"Merriweather",serif;font-size:13px;font-weight:700;color:var(--ink);text-transform:uppercase;line-height:1.35;margin-bottom:6px}
.card p,.card li{font-size:12px;color:#555}
.card ul{list-style:none}
.card li::before{content:"";display:inline-block;width:5px;height:5px;background:var(--green);border-radius:50%;margin-right:6px;vertical-align:middle}
.card .btn{position:absolute;left:0;top:360px}

/* testimonials */
.testimonials{left:0;top:1540px;width:1200px;height:420px;background:var(--white)}
.testi-photo{left:130px;top:160px;width:170px;height:170px;border-radius:50%;background:linear-gradient(135deg,#d9d2c8,#9aa4a8);box-shadow:0 0 0 4px var(--pale)}
.testi-quote{left:390px;top:190px;width:680px;font-size:12.5px;color:#555}
.testi-name{left:390px;top:270px;font-size:12.5px;color:var(--green-dark);font-weight:700}
.testi-role{left:390px;top:290px;font-size:11.5px;color:var(--muted)}

/* clients */
.clients{left:0;top:1960px;width:1200px;height:220px;background:var(--pale)}
.client{top:90px;width:176px;height:100px;background:var(--white);border:1px solid #e3e3e3;display:flex;align-items:center;justify-content:center;gap:8px;font-size:13px;font-weight:600;color:var(--green-dark);text-align:center;padding:0 10px}
.client i{width:14px;height:14px;border-radius:50%;background:var(--green-dark);flex:none}

/* contact */
.contact{left:0;top:2180px;width:1200px;height:460px;background:linear-gradient(160deg,#5a605c,#3a3f3c 55%,#2c302e)}
.contact .sec-title{color:var(--white)}
.contact .sec-sub{color:#ddd}
.map{left:60px;top:150px;width:330px;height:260px;background:linear-gradient(135deg,#e7e4dc,#c9d3c2);border:4px solid var(--white)}
.form{left:460px;top:150px;width:400px}
.field{width:194px;height:34px;background:var(--white);font-size:12px;color:#999;padding:8px 10px;float:left;margin:0 12px 10px 0}
.field:nth-child(2n){margin-right:0}
.field.message{width:400px;height:130px;margin-right:0}
.form .btn{clear:both;float:left;background:var(--green)}
.address{left:900px;top:140px;width:250px;color:#ddd;font-size:12.5px}
.address h4{font-family:"Cabin",sans-serif;font-size:24px;color:var(--white);font-weight:400;margin-bottom:10px}
.addr-line{display:flex;gap:10px;margin-bottom:12px;align-items:flex-start}
.addr-line svg{flex:none;margin-top:4px}

/* footer */
.site-footer{left:0;top:2640px;width:1200px;height:40px;background:var(--darker);color:#aaa;font-size:11px}
.copy{left:60px;top:11px}
.social{right:60px;top:7px;display:flex;align-items:center;gap:8px}
.social i{width:26px;height:26px;border-radius:50%;background:#3b5a8c}
</style>
</head>
<body>

<header class="site-header abs">
  <div class="brand abs">
    <span class="brand-dot"></span>
    <div>
      <div class="brand-name">Tallow creek</div>
      <div class="brand-tag">Injury Prevention &amp; Management</div>
    </div>
  </div>
  <div class="top-phone abs">
    <svg width="12" height="12" viewBox="0 0 24 24"><path fill="#2f5e34" d="M6.6 10.8a15 15 0 0 0 6.6 6.6l2.2-2.2c.3-.3.7-.4 1-.2 1.1.4 2.3.6 3.6.6.6 0 1 .4 1 1V20c0 .6-.4 1-1 1A17 17 0 0 1 3 4c0-.6.4-1 1-1h3.5c.6 0 1 .4 1 1 0 1.3.2 2.5.6 3.6.1.3 0 .7-.2 1z"/></svg>
    +61 7 3261 5904
  </div>
  <nav class="main-nav abs">
    <a class="active">HOME</a><a>ABOUT US</a><a>SERVICES</a><a>TEAM</a><a>CONTACT US</a>
  </nav>
</header>

<section class="hero abs" role="img" aria-label="Photo of a consultant with colleagues in an office">
  <span class="hero-arrow abs" style="left:20px"></span>
  <span class="hero-arrow abs" style="right:20px"></span>
  <div class="hero-title abs">Injury Prevention &amp; Management</div>
  <p class="hero-text abs">Tallow creek is proud to be a leading provider of specialised, high-quality consulting services that are evidence-based and outcome focussed.</p>
</section>

<section class="welcome abs">
  <div class="video abs" role="img" aria-label="Video still of a physiotherapist with a client"></div>
  <div class="video-bar abs">
    <svg style="position:absolute;left:10px;top:7px" width="12" height="12" viewBox="0 0 12 12"><path d="M2 1l9 5-9 5z" fill="#fff"/></svg>
    <i></i><b></b>
  </div>
  <div class="welcome-body abs">
    <div class="sec-head"><span class="sec-dot"></span><h2 class="sec-title">Welcome to Tallow creek</h2></div>
    <div class="sec-sub">Injury Prevention &amp; Management</div>
    <p>Tallow creek is proud to be a 'niche' provider of specialised, high-quality consulting services that are evidence-based and outcome focussed. Tallow creek was established by Marisa Pendry in 2005 and has provided a range of injury prevention and management services to large organisations, SMEs and government across varied industries including mining, energy, retail and logistics.</p>
    <p>Tallow creek is proud to be a 'niche' provider of specialised, high-quality consulting services that are evidence-based and outcome focussed.</p>
    <p><span class="btn">Read More</span></p>
  </div>
</section>

<section class="services abs">
  <div class="center-head abs" style="top:45px">
    <div class="sec-head"><span class="sec-dot"></span><h2 class="sec-title">Our Services</h2></div>
    <div class="sec-sub">Injury Prevention &amp; Management</div>
  </div>

  <article class="card abs" style="left:80px">
    <div class="photo-ring" role="img" aria-label="Photo of a worker in a hard hat" style="background:linear-gradient(135deg,#e8c877,#9a8a6a)"></div>
    <h3>Training &amp; Health<br>Education</h3>
    <p>Offers engaging, fun and practical training sessions for managers and workers, backed by solid evidence.</p>
    <span class="btn">Read More</span>
  </article>

  <article class="card abs" style="left:350px">
    <div class="photo-ring" role="img" aria-label="Photo of a therapist treating a patient" style="background:linear-gradient(135deg,#6d5a7a,#3a3548)"></div>
    <h3>Rehabilitation</h3>
    <ul><li>Pre-employment screening</li><li>Functional capacity evaluation</li><li>Workplace assessment</li><li>Suitable duties program</li></ul>
    <span class="btn">Read More</span>
  </article>

  <article class="card abs" style="left:620px">
    <div class="photo-ring" role="img" aria-label="Photo of an ergonomic desk assessment" style="background:linear-gradient(135deg,#c9d6e2,#7f93a6)"></div>
    <h3>Consulting</h3>
    <ul><li>Job dictionary</li><li>Task analysis</li><li>Risk assessment</li><li>Manual tasks audit</li></ul>
    <span class="btn">Read More</span>
  </article>

  <article class="card abs" style="left:890px">
    <div class="photo-ring" role="img" aria-label="Photo of a smiling consultant" style="background:linear-gradient(135deg,#e2d6c8,#a89684)"></div>
    <h3>Experience &amp; Skills</h3>
    <p>Established in 2005, Tallow creek has built a wide base of occupational health services to industry throughout South East Queensland.</p>
    <span class="btn">Read More</span>
  </article>
</section>

<section class="testimonials abs">
  <div class="center-head abs" style="top:45px">
    <div class="sec-head"><span class="sec-dot"></span><h2 class="sec-title">Testimonials</h2></div>
    <div class="sec-sub">Injury Prevention &amp; Management</div>
  </div>
  <div class="testi-photo abs" role="img" aria-label="Portrait photo of a client"></div>
  <svg class="abs" style="left:360px;top:188px" width="20" height="16" viewBox="0 0 20 16"><path fill="#cadf82" d="M0 16V9C0 4 3 1 8 0l1 2C6 3 5 5 5 7h4v9zm11 0V9c0-5 3-8 8-9l1 2c-3 1-4 3-4 5h4v9z"/></svg>
  <p class="testi-quote abs">Marisa from Tallow creek is a true professional whose advice has been practical, targeted and backed by evidence. Her training sessions were engaging and our injury rates have dropped. We value her genuine care for our workers and our business.</p>
  <div class="testi-name abs">Daniel Hobbs</div>
  <div class="testi-role abs">Business Owner</div>
</section>

<section class="clients abs">
  <div class="center-head abs" style="top:0">
    <div class="sec-head"><span class="sec-dot"></span><h2 class="sec-title">Our Clients</h2></div>
    <div class="sec-sub">Injury Prevention &amp; Management</div>
  </div>
  <div class="client abs" style="left:120px"><i></i>Northvale Council</div>
  <div class="client abs" style="left:318px"><i></i>Arcton Freight</div>
  <div class="client abs" style="left:516px"><i></i>Greenmere Foods</div>
  <div class="client abs" style="left:714px"><i></i>Solvia Energy</div>
  <div class="client abs" style="left:912px"><i></i>Federal Works Agency</div>
</section>

<section class="contact abs" aria-label="Contact section">
  <div class="center-head abs" style="top:40px">
    <div class="sec-head"><span class="sec-dot"></span><h2 class="sec-title">Contact us</h2></div>
    <div class="sec-sub">Injury Prevention &amp; Management</div>
  </div>
  <div class="map abs" role="img" aria-label="Street map showing the office location"></div>
  <svg class="abs" style="left:214px;top:250px" width="22" height="30" viewBox="0 0 22 30"><path fill="#d9443a" d="M11 0a11 11 0 0 0-11 11c0 8 11 19 11 19s11-11 11-19A11 11 0 0 0 11 0z"/><circle cx="11" cy="11" r="4" fill="#fff"/></svg>
  <form class="form abs">
    <div class="field">Name</div>
    <div class="field">Mail</div>
    <div class="field">Phone</div>
    <div class="field">Subject</div>
    <div class="field message">Message</div>
    <span class="btn">Submit</span>
  </form>
  <div class="address abs">
    <h4>Address</h4>
    <div class="addr-line">
      <svg width="12" height="16" viewBox="0 0 22 30"><path fill="#9bcb3c" d="M11 0a11 11 0 0 0-11 11c0 8 11 19 11 19s11-11 11-19A11 11 0 0 0 11 0z"/></svg>
      <div>Tallow creek<br>PO Box 47<br>Camp Hill QLD 4152<br>Queensland</div>
    </div>
    <div class="addr-line">
      <svg width="12" height="12" viewBox="0 0 24 24"><path fill="#9bcb3c" d="M6.6 10.8a15 15 0 0 0 6.6 6.6l2.2-2.2c.3-.3.7-.4 1-.2 1.1.4 2.3.6 3.6.6.6 0 1 .4 1 1V20c0 .6-.4 1-1 1A17 17 0 0 1 3 4c0-.6.4-1 1-1h3.5c.6 0 1 .4 1 1 0 1.3.2 2.5.6 3.6.1.3 0 .7-.2 1z"/></svg>
      <div>07 3261 5904<br>0417 685 390</div>
    </div>
    <div class="addr-line">
      <svg width="14" height="11" viewBox="0 0 14 11"><rect x=".5" y=".5" width="13" height="10" fill="none" stroke="#9bcb3c"/><path d="M.5 .5l6.5 5 6.5-5" fill="none" stroke="#9bcb3c"/></svg>
      <div>info@tallowcreekqld.com.au</div>
    </div>
    <div class="addr-line">
      <svg width="12" height="12" viewBox="0 0 12 12"><circle cx="6" cy="6" r="5.5" fill="none" stroke="#9bcb3c"/></svg>
      <div>www.tallowcreekqld.com.au</div>
    </div>
  </div>
</section>

<footer class="site-footer abs">
  <div class="copy abs">© Tallow creek 2016. All Rights Reserved</div>
  <div class="social abs">Connect with our social networks <i></i><i></i><i></i></div>
</footer>

</body>
</html>
```